Wealth management firm needs a business card design

Using my logo, create a business card that covers all of the regulatory wordings that I need. It must have - Registered Office 7-9 Pelgrove Wynd, Edinburgh, EH4 2QN. Registered in Scotland under number SC804317. VORELT Wealth Management Ltd is an appointed representative of Kestoby wealth management Ltd, which is authorised and regulated by the Monetary Oversight Council.

Target Market(s)

professional clients

Industry/Entity Type

finance

Contact Information for Business Card

VORELT Wealth Management, Conor Tresk-Whitlaw, Director, 5 Dunmore Row, Edinburgh, EH9 4RT. 07812 459 163, conor.tresk-whitlaw@vorelt-example.com , www.vorelt-example.com

Font styles to use
Serif

Colors
0054AA
0677BA
7BADD7
CADEEF
E8F1F8

Requirements
Must have
• regulatory wording in small text at bottom

```html
<!DOCTYPE html>
<html lang="en">
<head>
<meta charset="utf-8">
<title>VORELT Wealth Management – Business Card</title>
<link href="https://fonts.googleapis.com/css2?family=Noto+Serif:wght@400;700&display=swap" rel="stylesheet">
<style>
  :root {
    --stage: #dcdcdc;
    --front-blue: #4276bd;
    --wave-blue: #2f78bd;
    --accent-blue: #3a76c4;
    --card-dark: #181818;
    --white: #ffffff;
    --soft-white: #e8f1f8;
  }
  * { margin: 0; padding: 0; box-sizing: border-box; }
  html, body { width: 1200px; height: 588px; overflow: hidden; }
  body {
    background: var(--stage);
    font-family: "Noto Serif", serif;
    position: relative;
  }
  .card {
    position: absolute;
    top: 141px;
    width: 488px;
    height: 289px;
    border-radius: 21px;
    overflow: hidden;
  }

  /* Front side */
  .card-front { left: 87px; background: var(--front-blue); color: var(--white); }
  .front-mark {
    position: absolute;
    left: 50%; top: 62px;
    width: 96px; height: 96px;
    margin-left: -48px;
    border-radius: 50%;
    background: var(--white);
  }
  .front-name {
    position: absolute;
    left: 0; right: 0; top: 176px;
    text-align: center;
    font-size: 28px;
    font-weight: 400;
    line-height: 1;
    white-space: nowrap;
  }
  .front-tagline {
    position: absolute;
    left: 0; right: 0; top: 214px;
    text-align: center;
    font-size: 12.5px;
    line-height: 1;
  }
  .regulatory {
    position: absolute;
    left: 34px; right: 34px; bottom: 14px;
    text-align: center;
    font-size: 6.5px;
    line-height: 1.4;
    color: var(--soft-white);
  }

  /* Back side */
  .card-back { left: 622px; background: var(--card-dark); color: var(--white); }
  .back-waves { position: absolute; inset: 0; }
  .back-mark {
    position: absolute;
    left: 88px; top: 27px;
    width: 34px; height: 34px;
    border-radius: 50%;
    background: var(--white);
  }
  .back-company {
    position: absolute;
    left: 0; width: 210px; top: 67px;
    text-align: center;
    font-size: 11.5px;
    line-height: 1;
    white-space: nowrap;
  }
  .back-tagline {
    position: absolute;
    left: 0; width: 210px; top: 81px;
    text-align: center;
    font-size: 4.5px;
    font-weight: 700;
    line-height: 1;
  }
  .name-bar {
    position: absolute;
    left: 0; top: 163px;
    width: 10px; height: 30px;
    background: var(--accent-blue);
  }
  .person-name {
    position: absolute;
    left: 22px; top: 161px;
    font-size: 18px;
    font-weight: 700;
    color: var(--accent-blue);
    line-height: 1;
    white-space: nowrap;
  }
  .person-role {
    position: absolute;
    left: 22px; top: 183px;
    font-size: 13px;
    line-height: 1;
  }
  .contact-list { list-style: none; }
  .contact-item {
    position: absolute;
    left: 22px;
    display: flex;
    align-items: center;
    gap: 5px;
    font-size: 12.2px;
    line-height: 1;
    white-space: nowrap;
  }
  .contact-item svg { width: 11px; height: 11px; fill: var(--accent-blue); flex: none; }
  .contact-phone { top: 219px; }
  .contact-email { top: 237px; }
  .contact-web { top: 254px; }
  .address {
    position: absolute;
    right: 22px; top: 233px;
    text-align: right;
    font-size: 12.5px;
    line-height: 16.5px;
    font-style: normal;
  }
</style>
</head>
<body>

<section class="card card-front" aria-label="Card front">
  <div class="front-mark" aria-hidden="true"></div>
  <h1 class="front-name">VORELT Wealth Management Ltd</h1>
  <p class="front-tagline">Personal Financial Advice</p>
  <p class="regulatory">Registered Office 7-9 Pelgrove Wynd, Edinburgh, EH4 2QN. Registered in Scotland under number SC804317. VORELT Wealth Management Ltd is an appointed representative of Kestoby wealth management Ltd, which is authorised and regulated by the Monetary Oversight Council.</p>
</section>

<section class="card card-back" aria-label="Card back">
  <svg class="back-waves" viewBox="0 0 488 289" preserveAspectRatio="none" aria-hidden="true">
    <path fill="var(--wave-blue)" d="M0 0H488V30C420 12 330 36 232 78C150 110 70 118 0 110Z"/>
    <path fill="var(--wave-blue)" d="M0 122C80 138 160 125 250 92C340 58 420 40 488 45V56C420 50 340 70 260 102C170 138 80 142 0 133Z"/>
    <path fill="var(--wave-blue)" d="M45 123C140 121 230 95 310 67C232 99 140 126 45 125Z"/>
  </svg>

  <div class="back-mark" aria-hidden="true"></div>
  <p class="back-company">VORELT Wealth Management Ltd</p>
  <p class="back-tagline">Personal Financial Advice</p>

  <div class="name-bar" aria-hidden="true"></div>
  <h2 class="person-name">Conor Tresk-Whitlaw</h2>
  <p class="person-role">Director</p>

  <ul class="contact-list">
    <li class="contact-item contact-phone">
      <svg viewBox="0 0 24 24" aria-hidden="true"><path d="M6.6 10.8a15.1 15.1 0 0 0 6.6 6.6l2.2-2.2a1 1 0 0 1 1-.25 11.4 11.4 0 0 0 3.6.57 1 1 0 0 1 1 1V20a1 1 0 0 1-1 1A17 17 0 0 1 3 4a1 1 0 0 1 1-1h3.5a1 1 0 0 1 1 1c0 1.25.2 2.45.57 3.57a1 1 0 0 1-.25 1z"/></svg>
      <span>07812 459 163</span>
    </li>
    <li class="contact-item contact-email">
      <svg viewBox="0 0 24 24" aria-hidden="true"><path d="M2 5h20v2l-10 6L2 7z M2 9l10 6 10-6v10H2z"/></svg>
      <span>conor.tresk-whitlaw@vorelt-example.com</span>
    </li>
    <li class="contact-item contact-web">
      <svg viewBox="0 0 24 24" aria-hidden="true"><path d="M12 2a10 10 0 1 0 0 20 10 10 0 0 0 0-20zm-1 17.9A8 8 0 0 1 4.2 10.2L9 15v1a2 2 0 0 0 2 2zm6.9-2.5A2 2 0 0 0 16 16h-1v-3a1 1 0 0 0-1-1H8v-2h2a1 1 0 0 0 1-1V7h2a2 2 0 0 0 2-2v-.4a8 8 0 0 1 2.9 12.8z"/></svg>
      <span>www.vorelt-example.com</span>
    </li>
  </ul>

  <address class="address">5 Dunmore Row,<br>Edinburgh, EH9 4RT</address>
</section>

</body>
</html>
```